Tallow Electrical Business Card

We need a business card design for our family-run electrical contracting business based in Western Australia called 'Tallow Electrical'. We provide electrical services including residential, commercial and industrial. We aim for individual business cards to be made for all of our employees. We already have a company logo, which we require to be featured on the design. We would like simple, sleek and vibrant designs, which incorporate our logo and represent our business. We do not want anything involving too many graphics/images. We like the colours red, black, white and all shades of grey. The final design should communicate professionalism and trustworthiness.
We require the following contact information:
Name- Peter Hargreave
EC 5810
Mobile number- 0455 902 318
Fax number (including area code)- (08) 9576 2083
Email adress- name@tallowelectric.com.au
Industry/Entity Type
Electrical
Font styles to use
Other font styles liked:
- ITC Handel Bold
Look and feel

```html
<!DOCTYPE html>
<html lang="en">
<head>
<meta charset="utf-8">
<title>Tallow Electrical Business Card</title>
<link rel="stylesheet" href="https://fonts.googleapis.com/css2?family=Exo+2:wght@400;500;700&display=swap">
<style>
  :root {
    --backdrop: #e4e4e4;
    --brand-red: #e0262b;
    --brand-red-light: #ee4a4a;
    --card-white: #ffffff;
    --ink: #1f1f1f;
    --on-red: #ffffff;
  }
  * { box-sizing: border-box; margin: 0; padding: 0; }
  html, body {
    width: 1200px; height: 1023px; overflow: hidden;
    background: var(--backdrop);
    font-family: "Exo 2", Arial, sans-serif;
  }
  .business-card {
    position: absolute; left: 170px; top: 261px;
    width: 860px; height: 500px;
    display: flex;
    box-shadow: 0 10px 30px rgba(0,0,0,0.18);
  }
  .contact-panel {
    width: 440px; height: 100%;
    background: linear-gradient(160deg, var(--brand-red) 0%, var(--brand-red-light) 55%, var(--brand-red) 100%);
    color: var(--on-red);
    padding: 56px 40px 0 48px;
  }
  .holder-name {
    font-weight: 700; font-size: 40px; letter-spacing: 0.5px;
    margin-bottom: 48px;
  }
  .licence {
    font-size: 22px; font-weight: 500; margin-bottom: 24px;
  }
  .contact-row {
    display: flex; align-items: center; gap: 18px;
    font-size: 22px; font-weight: 500; margin-bottom: 18px;
  }
  .contact-icon { width: 50px; height: 50px; flex: none; }
  .contact-row.email { font-size: 19px; }
  .brand-panel {
    flex: 1; background: var(--card-white);
    display: flex; align-items: center; justify-content: center; gap: 22px;
  }
  .brand-square {
    width: 34px; height: 34px; background: var(--brand-red);
  }
  .brand-name {
    font-weight: 700; font-size: 52px; color: var(--ink);
    letter-spacing: 2px; line-height: 1;
  }
</style>
</head>
<body>
  <section class="business-card">
    <div class="contact-panel">
      <h1 class="holder-name">Peter Hargreave</h1>
      <p class="licence">EC 5810</p>
      <p class="contact-row">
        <svg class="contact-icon" viewBox="0 0 50 50" aria-hidden="true">
          <circle cx="25" cy="25" r="23" fill="none" stroke="#fff" stroke-width="2.5"/>
          <rect x="18" y="12" width="14" height="26" rx="2.5" fill="none" stroke="#fff" stroke-width="2.5"/>
          <line x1="22" y1="33" x2="28" y2="33" stroke="#fff" stroke-width="2.5"/>
        </svg>
        <span>0455 902 318</span>
      </p>
      <p class="contact-row">
        <svg class="contact-icon" viewBox="0 0 50 50" aria-hidden="true">
          <circle cx="25" cy="25" r="23" fill="none" stroke="#fff" stroke-width="2.5"/>
          <rect x="18" y="12" width="14" height="8" fill="none" stroke="#fff" stroke-width="2.5"/>
          <rect x="13" y="20" width="24" height="14" rx="2" fill="none" stroke="#fff" stroke-width="2.5"/>
          <rect x="18" y="30" width="14" height="8" fill="none" stroke="#fff" stroke-width="2.5"/>
        </svg>
        <span>(08) 9576 2083</span>
      </p>
      <p class="contact-row email">
        <svg class="contact-icon" viewBox="0 0 50 50" aria-hidden="true">
          <circle cx="25" cy="25" r="23" fill="none" stroke="#fff" stroke-width="2.5"/>
          <rect x="12" y="16" width="26" height="18" fill="none" stroke="#fff" stroke-width="2.5"/>
          <polyline points="12,16 25,27 38,16" fill="none" stroke="#fff" stroke-width="2.5"/>
        </svg>
        <span>name@tallowelectric.com.au</span>
      </p>
    </div>
    <div class="brand-panel">
      <span class="brand-square" aria-hidden="true"></span>
      <span class="brand-name">Tallow Electrical</span>
    </div>
  </section>
</body>
</html>
```